依頼詳細
<取扱商品>
レディースバレエシューズ・ルームシューズ・除菌スプレー・マスクケースなど

<ターゲット>
やや女性向け
基本は老若男女問わず

<使用画像について>
商品画像はコンペ終了後にお渡ししますので仮の画像を入れていただければと思います。
商品画像以外の使用素材は有料のものでも問題は有りませんが、quilva picsまたは低価格(0~2000円程度)のものでお願いします。
※もし有料素材を使う場合は最初から購入して頂く必要はないのでウォーターマーク付きのもので提案していただければ大丈夫です。

<デザイン>
明るめのやさしい感じでお願いします。
参考サイトほどピンクは強めでなくてもいいかと思いますが、デザイン次第では濃い色の使用もありかと思います。

参考サイト
https://pelrovin.jp/

<ページ幅>
1920pxでお願いします。

<特筆事項>
今回NIVOを使用するにあたりプラン的にNIVOマークが必須になります。
右上のテントのマークはありきでお願いします。

今後も定期的にデザインをお願いすることができる技量を持つ方を探しておりますので是非、単発と考えずにデザインを出していただければと思います。
それでは皆様のご応募よろしくお願い致します。
サイトURL
ページ数
1ページ
希望イメージ
シンプル 複雑
単色 カラフル
暗い 明るい
日常 高級
遊び心 厳粛
未来的 伝統的
女性的 男性的
希望する色
白・淡いピンク・淡い水色などの優しい色
納品ファイル
• フォトショップ形式 (.psd)
補足説明
■ 選んだ理由

こちらが想定した以上のデザインでした。

■ 提案者全員のお礼・コメント

この度は当方コンペにご提案いただきありがとうございました。
提案頂いた方々のデザインはどれも素敵なもので、真剣に吟味し当選者を選択させていただきました。
今後もミルトカを利用してのデザインコンペを行う予定ですので、残念ながら今回は当選とならなかった方もまたご参加いただけると幸いです。
今後もどうかよろしくお願い致します。

```html
<!DOCTYPE html>
<html lang="ja">
<head>
<meta charset="utf-8">
<title>ruvelle</title>
<link rel="stylesheet" href="https://fonts.googleapis.com/css2?family=Cormorant+Garamond:ital,wght@0,400;0,500;1,400&family=Noto+Serif+JP:wght@300;400;500&display=swap">
<style>
:root{
  --white:#ffffff;
  --ink:#4a4340;
  --ink-soft:#7a716c;
  --accent:#e98a7f;
  --button:#ec8f86;
  --cream:#fdf6dc;
  --blush:#fbe3dc;
  --panel-pink:#f4a39a;
  --panel-peach:#f8c39c;
  --panel-yellow:#f8d97f;
  --footer:#fbeee6;
}
*{margin:0;padding:0;box-sizing:border-box}
html,body{width:1200px;height:2788px;overflow:hidden}
body{font-family:"Noto Serif JP",serif;color:var(--ink);background:var(--white);position:relative}

.hero{position:absolute;left:0;top:0;width:1200px;height:600px;
  background:linear-gradient(100deg,#f1efee 0%,#e6e3e1 40%,#bdb3ac 62%,#8f8580 80%,#d7d1cc 100%)}
.hero-floor{position:absolute;left:0;bottom:0;width:100%;height:260px;background:linear-gradient(180deg,rgba(255,255,255,0),rgba(238,236,234,.9))}
.site-nav{position:absolute;left:36px;top:38px;display:flex;gap:30px;font-size:12px;color:var(--white);letter-spacing:.08em;z-index:2}
.site-logo{position:absolute;left:560px;top:16px;font-family:"Cormorant Garamond",serif;font-size:50px;font-weight:400;color:var(--white);letter-spacing:.04em;z-index:2}
.hero-caption{position:absolute;left:560px;top:404px;font-family:"Cormorant Garamond",serif;font-size:26px;color:var(--white);letter-spacing:.06em;z-index:2}

.brand{position:absolute;left:0;top:600px;width:1200px;height:420px;text-align:center;background:var(--white)}
.section-mark{display:block;margin:0 auto}
.brand .section-mark{margin-top:62px}
.section-title{font-family:"Cormorant Garamond",serif;font-weight:400;font-size:38px;color:var(--accent);letter-spacing:.03em}
.brand .section-title{margin-top:6px}
.brand-text{margin-top:36px;font-size:13px;line-height:2.35;color:var(--ink);letter-spacing:.08em}

.products{position:absolute;left:0;top:1020px;width:1200px;height:1440px;
  background:linear-gradient(90deg,var(--cream) 0%,#fdf3e0 45%,var(--blush) 100%)}
.products .section-mark{margin-top:46px}
.products .section-title{text-align:center;margin-top:4px}
.product-grid{position:absolute;left:28px;top:180px;width:1144px;display:grid;grid-template-columns:560px 560px;gap:12px 24px}
.product-card{position:relative;height:520px;border-radius:26px;overflow:hidden}
.product-photo{position:absolute;inset:0}
.card-valley .product-photo{background:linear-gradient(160deg,#8ea3b8 0%,#b5a79a 45%,#b9392f 70%,#c9b8a4 100%)}
.card-room .product-photo{background:linear-gradient(170deg,#1f3a4a 0%,#5b5f4e 45%,#c88a3a 70%,#b48a5e 100%)}
.card-spray .product-photo{background:linear-gradient(150deg,#d9d8d6 0%,#f4f3f1 45%,#e7c9b6 75%,#cfcac6 100%)}
.card-mask .product-photo{background:linear-gradient(140deg,#3f4f5e 0%,#7a857c 40%,#d8c9a2 60%,#c9d06a 85%,#8e8a72 100%)}
.product-label{position:absolute;left:0;bottom:8px;width:390px;height:42px;background:var(--white);display:flex;align-items:center;padding:0 18px;gap:14px}
.product-name{font-family:"Cormorant Garamond",serif;font-size:19px;color:var(--ink)}
.product-sub{font-size:10px;color:var(--ink-soft);flex:1;letter-spacing:.06em}
.arrow{width:26px;height:8px}

.more-button{position:absolute;left:412px;top:1292px;width:376px;height:76px;background:var(--button);color:var(--white);font-size:17px;letter-spacing:.16em;display:flex;align-items:center;justify-content:center}

.info-panels{position:absolute;left:0;top:2460px;width:1200px;height:260px;display:flex}
.info-panel{flex:1;display:flex;flex-direction:column;align-items:center;justify-content:center;color:var(--white);gap:26px;font-size:13px;letter-spacing:.14em}
.panel-about{background:var(--panel-pink)}
.panel-contact{background:var(--panel-peach)}
.panel-faq{background:var(--panel-yellow)}
.about-box{width:140px;height:46px;border:2px solid var(--white);display:flex;align-items:center;justify-content:center;font-family:"Cormorant Garamond",serif;font-size:20px;letter-spacing:.1em}
.faq-word{font-family:"Cormorant Garamond",serif;font-size:44px;font-weight:500;letter-spacing:.06em;height:52px;line-height:52px}

.site-footer{position:absolute;left:0;top:2720px;width:1200px;height:68px;background:var(--footer);display:flex;align-items:center;padding:0 30px;gap:60px;font-size:10px;color:var(--ink-soft);letter-spacing:.06em}
</style>
</head>
<body>

<header class="hero">
  <div class="hero-floor" role="img" aria-label="Woman in a floral skirt wearing red ballet shoes on a white floor"></div>
  <nav class="site-nav"><span>会社概要</span><span>商品一覧</span><span>よくある質問</span><span>お問い合わせ</span></nav>
  <div class="site-logo">ruvelle</div>
  <p class="hero-caption">dummy semi square shoes collection</p>
</header>

<section class="brand">
  <svg class="section-mark" width="24" height="26" viewBox="0 0 24 26"><path d="M12 24 C10 16 6 10 4 4 M12 24 C13 15 17 9 20 4 M12 24 C12 16 12 8 12 2" stroke="#e98a7f" stroke-width="1.6" fill="none" stroke-linecap="round"/></svg>
  <h2 class="section-title">Brand message</h2>
  <p class="brand-text">
    ruvelleは毎日の歩みにそっと寄り添う靴と雑貨をお届けします。<br>
    「やさしく、心地よく」を大切に、ひとつひとつ丁寧に作りました。<br>
    履き心地のよさと、上質な素材と美しさにこだわったものばかりです。<br>
    軽やかな足どりで、いつもの日常が少しだけ明るくなりますように。<br>
    家の中でも外でも、心地よく過ごせる時間を。<br>
    あなたの毎日がもっと楽しくなるよう心を込めてお届けいたします。
  </p>
</section>

<section class="products">
  <svg class="section-mark" width="24" height="26" viewBox="0 0 24 26"><path d="M12 24 C10 16 6 10 4 4 M12 24 C13 15 17 9 20 4 M12 24 C12 16 12 8 12 2" stroke="#e98a7f" stroke-width="1.6" fill="none" stroke-linecap="round"/></svg>
  <h2 class="section-title">Products</h2>

  <div class="product-grid">
    <article class="product-card card-valley">
      <div class="product-photo" role="img" aria-label="Red heeled ballet shoes worn with cropped denim on a stone floor"></div>
      <div class="product-label"><span class="product-name">Valley shoes</span><span class="product-sub">バレエシューズ</span>
        <svg class="arrow" viewBox="0 0 26 8"><path d="M0 6.5H24L18 1" stroke="#4a4340" stroke-width="1.3" fill="none"/></svg></div>
    </article>
    <article class="product-card card-room">
      <div class="product-photo" role="img" aria-label="Mustard room shoes worn with dark trousers on a patterned rug"></div>
      <div class="product-label"><span class="product-name">Room shoes</span><span class="product-sub">ルームシューズ</span>
        <svg class="arrow" viewBox="0 0 26 8"><path d="M0 6.5H24L18 1" stroke="#4a4340" stroke-width="1.3" fill="none"/></svg></div>
    </article>
    <article class="product-card card-spray">
      <div class="product-photo" role="img" aria-label="Hand holding a white disinfectant spray bottle"></div>
      <div class="product-label"><span class="product-name">Disinfectant spray</span><span class="product-sub">除菌スプレー</span>
        <svg class="arrow" viewBox="0 0 26 8"><path d="M0 6.5H24L18 1" stroke="#4a4340" stroke-width="1.3" fill="none"/></svg></div>
    </article>
    <article class="product-card card-mask">
      <div class="product-photo" role="img" aria-label="Fabric mask cases in navy, beige and yellow laid flat"></div>
      <div class="product-label"><span class="product-name">Mask case</span><span class="product-sub">マスクケース</span>
        <svg class="arrow" viewBox="0 0 26 8"><path d="M0 6.5H24L18 1" stroke="#4a4340" stroke-width="1.3" fill="none"/></svg></div>
    </article>
  </div>

  <a class="more-button">商品一覧</a>
</section>

<section class="info-panels">
  <div class="info-panel panel-about"><div class="about-box">ABOUT</div><span>会社概要</span></div>
  <div class="info-panel panel-contact">
    <svg width="64" height="52" viewBox="0 0 64 52"><rect x="2" y="2" width="60" height="42" fill="none" stroke="#fff" stroke-width="2.4"/><path d="M2 2 L32 26 L62 2" fill="none" stroke="#fff" stroke-width="2.4"/></svg>
    <span>お問い合わせ</span></div>
  <div class="info-panel panel-faq"><div class="faq-word">FAQ</div><span>よくある質問</span></div>
</section>

<footer class="site-footer"><span>株式会社ルヴェル</span><span>プライバシーポリシー</span><span>© ruvelle</span></footer>

</body>
</html>
```